Purpose, Mission, and Values Poster Update

Bridgewell Quality Labs, a Testing, Inspection, and Certification company in the Atlanta area, needs an updated PMV poster. Looking to update graphics and presentation, moving away from current design. Want to carry over company logo, colors (you can include additional blues in the design beyond what is mentioned in the brand guidelines as the previous design did), and messaging (see attachments).

We would also like a companion poster, using the same design language, that shows our goals for leads and won opportunities. Want to carry over logo, colors, and messaging from original, except for this one we want the leads goal to be 115 instead of 85.

Both posters need to be 6000w x 7200h at 300ppi, CMYK. We want to move away from the cartoony, corporate clipart sort of look that the current design has, as new leadership doesn't like the aesthetic.

Target Market(s)

Internal - group of engineers, chemists, scientists, and other technical personnel

Industry/Entity Type

TIC (Testing, Inspection, Certification)

Font styles to use
Serif
Sans Serif

Colors
0054AA
0677BA
7BADD7
CADEEF
E8F1F8

Requirements
Must have
• For both: CMYK colors for printing, 6000w x 7200h at 300ppi for poster sizing leads, company logo; for PMV poster: phrasing of purpose, mission, and values statements preserved; for ring the bell poster: leads goal updated to 115, opportunities goal unchanged at 25
Should not have
• Corporate clipart, cartoon characters

```html
<!DOCTYPE html>
<html lang="en">
<head>
<meta charset="utf-8">
<title>Bridgewell Quality Labs – Purpose, Mission, Values and Ring the Bell Posters</title>
<link rel="stylesheet" href="https://fonts.googleapis.com/css2?family=Montserrat:wght@300;400;600;700;800&family=Roboto+Condensed:wght@700&family=Roboto:wght@400;700&display=swap">
<style>
  :root{
    --stage:#9a9a9a;
    --navy-deep:#04152b;
    --navy:#0a3366;
    --brand-blue:#0054AA;
    --mid-blue:#0677BA;
    --sky:#2aa3e6;
    --soft-blue:#7BADD7;
    --pale-blue:#CADEEF;
    --ice:#E8F1F8;
    --white:#ffffff;
  }
  html,body{margin:0;padding:0;overflow:hidden;}
  body{width:1200px;height:823px;background:var(--stage);position:relative;}
  .poster{position:absolute;top:144px;width:446px;height:536px;box-shadow:0 12px 28px rgba(0,0,0,.35);}
  .poster svg{display:block;width:100%;height:100%;}
  .poster--pmv{left:124px;}
  .poster--bell{left:629px;}
  .heading{font-family:'Montserrat',sans-serif;fill:var(--white);}
  .heading--light{font-weight:300;}
  .heading--bold{font-weight:700;}
  .body-copy{font-family:'Roboto',sans-serif;fill:var(--white);}
  .value-title{font-family:'Roboto',sans-serif;font-weight:700;fill:var(--white);font-size:7px;text-anchor:middle;}
  .value-copy{font-family:'Roboto',sans-serif;fill:var(--ice);font-size:4.6px;text-anchor:middle;}
  .brand-name{font-family:'Montserrat',sans-serif;font-weight:700;fill:var(--white);font-size:8.5px;text-anchor:end;}
  .display{font-family:'Roboto Condensed',sans-serif;font-weight:700;fill:var(--sky);}
  .frame{fill:none;stroke:var(--pale-blue);stroke-width:1;}
  .accent{fill:var(--sky);}
  .icon-line{fill:none;stroke:var(--white);stroke-width:2.4;stroke-linecap:round;stroke-linejoin:round;}
  .icon-thin{fill:none;stroke:var(--white);stroke-width:1.3;stroke-linecap:round;stroke-linejoin:round;}
</style>
</head>
<body>

<!-- Purpose, Mission & Values poster -->
<section class="poster poster--pmv" aria-label="Purpose, Mission and Values poster">
<svg viewBox="0 0 372 447" xmlns="http://www.w3.org/2000/svg">
  <defs>
    <radialGradient id="poster-bg" cx="50%" cy="45%" r="75%">
      <stop offset="0" stop-color="#0d4f8f"/>
      <stop offset=".55" stop-color="#0a2f5c"/>
      <stop offset="1" stop-color="#04152b"/>
    </radialGradient>
  </defs>
  <rect width="372" height="447" fill="url(#poster-bg)"/>

  <!-- purpose block -->
  <rect class="frame" x="22" y="17" width="325" height="106" rx="9"/>
  <rect class="accent" x="30" y="34" width="17" height="76"/>
  <g class="purpose-icon">
    <circle cx="75" cy="73" r="28" fill="var(--white)"/>
    <circle cx="75" cy="73" r="20" fill="none" stroke="var(--navy)" stroke-width="4"/>
    <circle cx="75" cy="73" r="11" fill="none" stroke="var(--navy)" stroke-width="4"/>
    <circle cx="75" cy="73" r="3.5" fill="var(--navy)"/>
    <line x1="76" y1="72" x2="100" y2="48" stroke="var(--navy)" stroke-width="3"/>
    <path d="M96 46 L104 38 L105 45 L112 46 L104 54 Z" fill="var(--white)" stroke="var(--navy)" stroke-width="1.5"/>
  </g>
  <text class="heading heading--light" x="129" y="58" font-size="18">OUR</text>
  <text class="heading heading--bold" x="128" y="87" font-size="30">PURPOSE</text>
  <text class="body-copy" x="129" y="101" font-size="7.5">Create a safe and</text>
  <text class="body-copy" x="129" y="111" font-size="7.5">reliable world</text>
  <text class="brand-name" x="337" y="38">Bridgewell</text>
  <text class="brand-name" x="337" y="49">Quality Labs</text>

  <!-- mission block -->
  <rect class="frame" x="22" y="123" width="325" height="106" rx="9"/>
  <g class="mission-icon">
    <line class="icon-line" x1="50" y1="140" x2="50" y2="198"/>
    <circle cx="50" cy="139" r="4" fill="var(--white)"/>
    <path d="M52 145 C70 138 84 152 112 142 L100 158 L110 172 C84 180 70 166 52 173 Z" fill="var(--white)"/>
    <rect class="accent" x="40" y="196" width="20" height="9"/>
    <rect x="36" y="203" width="28" height="4" fill="var(--white)"/>
  </g>
  <text class="heading heading--light" x="129" y="153" font-size="18">OUR</text>
  <text class="heading heading--bold" x="128" y="179" font-size="30">MISSION</text>
  <text class="body-copy" x="129" y="199" font-size="7.5">Deliver assurance through precise</text>
  <text class="body-copy" x="129" y="209" font-size="7.5">technical and professional services</text>

  <!-- values block -->
  <rect class="frame" x="22" y="229" width="325" height="199" rx="9"/>
  <text class="heading heading--bold" x="184" y="268" font-size="29" text-anchor="middle">OUR VALUES</text>

  <text class="value-title" x="108" y="292">Keep People First</text>
  <text class="value-copy" x="108" y="300">Foster a collaborative and</text>
  <text class="value-copy" x="108" y="306">inclusive environment for team</text>
  <text class="value-copy" x="108" y="312">members growth</text>

  <text class="value-title" x="181" y="292">Think Global, Act Local</text>
  <text class="value-copy" x="181" y="300">Utilize our combined expertise</text>
  <text class="value-copy" x="181" y="306">and knowledge to deliver</text>
  <text class="value-copy" x="181" y="312">when and where</text>

  <text class="value-title" x="256" y="292">Do What's Right</text>
  <text class="value-copy" x="256" y="300">Hold ourselves accountable to</text>
  <text class="value-copy" x="256" y="306">the highest safety, professional</text>
  <text class="value-copy" x="256" y="312">and personal standards</text>

  <!-- connector band -->
  <path d="M62 352 Q179 392 296 352" fill="none" stroke="var(--mid-blue)" stroke-width="8"/>
  <path d="M62 344 Q179 304 296 344" fill="none" stroke="var(--sky)" stroke-width="4"/>
  <g stroke="var(--soft-blue)" stroke-width="1">
    <line x1="90" y1="316" x2="90" y2="328"/>
    <line x1="179" y1="316" x2="179" y2="328"/>
    <line x1="268" y1="316" x2="268" y2="328"/>
    <line x1="134" y1="366" x2="134" y2="376"/>
    <line x1="224" y1="366" x2="224" y2="368"/>
  </g>

  <g class="value-badges">
    <circle cx="90" cy="347" r="18" fill="var(--navy)" stroke="var(--white)" stroke-width="3"/>
    <circle cx="134" cy="347" r="18" fill="var(--navy)" stroke="var(--white)" stroke-width="3"/>
    <circle cx="179" cy="347" r="18" fill="var(--navy)" stroke="var(--white)" stroke-width="3"/>
    <circle cx="224" cy="347" r="18" fill="var(--navy)" stroke="var(--white)" stroke-width="3"/>
    <circle cx="268" cy="347" r="18" fill="var(--navy)" stroke="var(--white)" stroke-width="3"/>
    <!-- team -->
    <g class="icon-thin">
      <circle cx="84" cy="343" r="3"/><circle cx="96" cy="343" r="3"/><circle cx="90" cy="340" r="3.4"/>
      <path d="M80 354 Q84 347 88 352 M92 352 Q96 347 100 354 M85 356 Q90 346 95 356"/>
    </g>
    <!-- stars -->
    <g fill="var(--white)">
      <path d="M134 337 l1.6 3.3 3.6.5 -2.6 2.5 .6 3.6 -3.2-1.7 -3.2 1.7 .6-3.6 -2.6-2.5 3.6-.5z"/>
      <path d="M126 344 l1 2 2.2.3 -1.6 1.5 .4 2.2 -2-1 -2 1 .4-2.2 -1.6-1.5 2.2-.3z"/>
      <path d="M142 344 l1 2 2.2.3 -1.6 1.5 .4 2.2 -2-1 -2 1 .4-2.2 -1.6-1.5 2.2-.3z"/>
    </g>
    <path class="icon-thin" d="M127 357 L141 357 M130 353 L138 353"/>
    <!-- globe -->
    <g class="icon-thin">
      <circle cx="179" cy="347" r="9"/>
      <ellipse cx="179" cy="347" rx="4" ry="9"/>
      <line x1="170" y1="347" x2="188" y2="347"/>
    </g>
    <!-- diamond -->
    <path class="icon-thin" d="M216 343 L220 338 L228 338 L232 343 L224 355 Z M216 343 L232 343 M220 338 L224 355 L228 338"/>
    <!-- scales -->
    <g class="icon-thin">
      <line x1="268" y1="337" x2="268" y2="356"/>
      <line x1="259" y1="341" x2="277" y2="341"/>
      <line x1="263" y1="357" x2="273" y2="357"/>
      <path d="M259 341 L255 349 L263 349 Z M277 341 L273 349 L281 349 Z"/>
    </g>
  </g>

  <text class="value-title" x="134" y="388">Deliver Service Excellence</text>
  <text class="value-copy" x="134" y="396">Provide best-in-class</text>
  <text class="value-copy" x="134" y="402">experiences for our clients</text>

  <text class="value-title" x="224" y="378">Create Value</text>
  <text class="value-copy" x="224" y="386">Work efficiently and effectively to</text>
  <text class="value-copy" x="224" y="392">deliver quality results in</text>
  <text class="value-copy" x="224" y="398">complex environments.</text>
</svg>
</section>

<!-- Ring the Bell poster -->
<section class="poster poster--bell" aria-label="Ring the Bell goals poster">
<svg viewBox="0 0 372 447" xmlns="http://www.w3.org/2000/svg">
  <defs>
    <radialGradient id="poster-bg-2" cx="50%" cy="45%" r="75%">
      <stop offset="0" stop-color="#0d4f8f"/>
      <stop offset=".55" stop-color="#0a2f5c"/>
      <stop offset="1" stop-color="#04152b"/>
    </radialGradient>
  </defs>
  <rect width="372" height="447" fill="url(#poster-bg-2)"/>

  <!-- headline block -->
  <rect class="frame" x="22" y="17" width="325" height="111" rx="9"/>
  <text class="body-copy" x="37" y="42" font-size="7.6" font-weight="700">CELEBRATING OUR OPPORTUNITIES TO CREATE</text>
  <text class="brand-name" x="337" y="42">Bridgewell</text>
  <text class="brand-name" x="337" y="53">Quality Labs</text>
  <text class="display" x="36" y="78" font-size="33">A SAFE &amp;</text>
  <text class="display" x="36" y="112" font-size="33">RELIABLE WORLD</text>

  <!-- bell block -->
  <rect class="frame" x="22" y="128" width="325" height="104" rx="9"/>
  <text class="display" x="46" y="164" font-size="14" font-weight="400" style="font-family:'Montserrat',sans-serif;font-weight:400">WE</text>
  <text class="heading heading--bold" x="44" y="201" font-size="36">Ring</text>
  <g class="bell-icon">
    <path class="icon-line" d="M171 200 L171 181 Q171 160 190 158 Q209 160 209 181 L209 200 L214 206 L166 206 Z"/>
    <line class="icon-line" x1="190" y1="150" x2="190" y2="157"/>
    <circle cx="190" cy="213" r="3.5" fill="none" stroke="var(--white)" stroke-width="2.4"/>
    <path d="M163 166 Q158 176 161 186 M156 161 Q149 176 154 191" fill="none" stroke="var(--sky)" stroke-width="2.4" stroke-linecap="round"/>
    <path d="M217 166 Q222 176 219 186 M224 161 Q231 176 226 191" fill="none" stroke="var(--sky)" stroke-width="2.4" stroke-linecap="round"/>
  </g>
  <text class="display" x="244" y="164" font-size="14" style="font-family:'Montserrat',sans-serif;font-weight:400">THE</text>
  <text class="heading heading--bold" x="243" y="201" font-size="36">Bell</text>

  <!-- goals block -->
  <path class="frame" d="M22 232 L22 420 Q22 430 32 430 L176 430"/>
  <path class="frame" d="M347 232 L347 410"/>

  <g class="goal goal--leads">
    <path d="M80 266 L236 266 L262 302 L322 302" fill="none" stroke="var(--sky)" stroke-width="1.6"/>
    <path d="M80 318 L322 318" fill="none" stroke="var(--sky)" stroke-width="1.6"/>
    <path d="M318 298 L324 302 L318 306 Z M318 314 L324 318 L318 322 Z" fill="var(--sky)"/>
    <circle cx="80" cy="292" r="28" fill="var(--white)"/>
    <circle cx="80" cy="292" r="23" fill="var(--mid-blue)"/>
    <g class="icon-thin">
      <path d="M73 294 L73 301 Q80 308 87 301 L87 294"/>
      <line x1="70" y1="294" x2="76" y2="294"/><line x1="84" y1="294" x2="90" y2="294"/>
      <circle cx="71" cy="280" r="2"/><circle cx="80" cy="278" r="2"/><circle cx="89" cy="280" r="2"/>
      <path d="M67 287 Q71 282 75 287 M76 285 Q80 280 84 285 M85 287 Q89 282 93 287"/>
    </g>
    <text class="heading heading--bold" x="124" y="283" font-size="15">WHEN</text>
    <text class="heading heading--bold" x="124" y="300" font-size="15">WE'VE HIT</text>
    <text class="display" x="264" y="290" font-size="30" style="font-family:'Montserrat',sans-serif;font-weight:400">115</text>
    <text class="body-copy" x="266" y="300" font-size="7.5" font-weight="700">LEADS</text>
  </g>

  <g class="goal goal--won">
    <path d="M80 346 L236 346 L262 382 L322 382" fill="none" stroke="var(--sky)" stroke-width="1.6"/>
    <path d="M80 398 L322 398" fill="none" stroke="var(--sky)" stroke-width="1.6"/>
    <path d="M318 378 L324 382 L318 386 Z M318 394 L324 398 L318 402 Z" fill="var(--sky)"/>
    <circle cx="80" cy="372" r="28" fill="var(--white)"/>
    <circle cx="80" cy="372" r="23" fill="var(--mid-blue)"/>
    <g class="icon-thin">
      <path d="M80 357 l1.8 3.6 4 .6 -2.9 2.8 .7 4 -3.6-1.9 -3.6 1.9 .7-4 -2.9-2.8 4-.6z"/>
      <path d="M68 368 L72 380 L88 380 L92 368"/>
      <line x1="72" y1="384" x2="88" y2="384"/>
    </g>
    <text class="heading heading--bold" x="124" y="363" font-size="15">WHEN</text>
    <text class="heading heading--bold" x="124" y="380" font-size="15">WE'VE WON</text>
    <text class="display" x="264" y="370" font-size="30" style="font-family:'Montserrat',sans-serif;font-weight:400">25</text>
    <text class="body-copy" x="266" y="380" font-size="7.5" font-weight="700">OPPORTUNITIES</text>
  </g>

  <!-- web address pill -->
  <rect x="176" y="410" width="162" height="20" rx="10" fill="none" stroke="var(--pale-blue)" stroke-width="1"/>
  <text class="display" x="257" y="424" font-size="10" text-anchor="middle" letter-spacing="1.5" style="font-family:'Montserrat',sans-serif;font-weight:600">www.bridgewelllabs.com</text>
</svg>
</section>

</body>
</html>
```